Hi, Looking for an upgraded business card to the aged one attached. Open to suggestions and no real limitations, but if your going to use a picture of a taxi i think it should be vector based rather than a full color picture. I've uploaded a 2 pictures of the type of taxi which is a Velmora K7 in white. The taxi markings look like the pink one in the picture but to be clear his is white. The taxi is in Bermuda so if you wanted to include something island based that's ok as well but not required. The other thing he wanted to keep on there was the Island Watch, with the retired police office incorporated somehow.

Requirements
Must have
• Bermuda Taxi Operator
Retired Police Officer
Police Crest
Taxi #
Email
Mobile Number

```html
<!DOCTYPE html>
<html lang="en">
<head>
<meta charset="utf-8">
<title>Taxi Operator Business Card</title>
<link href="https://fonts.googleapis.com/css2?family=Roboto:wght@400;500;700&display=swap" rel="stylesheet">
<style>
  :root {
    --navy: #123f86;
    --navy-edge: #0d3a7a;
    --ink-blue: #2a56a0;
    --paper: #ffffff;
    --charcoal: #3a3a3a;
    --stage: #e9e9e9;
    --faint: rgba(255,255,255,0.22);
  }
  html, body {
    margin: 0;
    width: 1200px;
    height: 801px;
    overflow: hidden;
    background: var(--stage);
    font-family: "Roboto", Arial, sans-serif;
  }
  .sheet {
    position: relative;
    width: 1200px;
    height: 801px;
    display: flex;
    align-items: center;
    justify-content: center;
    gap: 40px;
  }
  .card {
    position: relative;
    width: 540px;
    height: 309px;
    box-sizing: border-box;
    overflow: hidden;
    border-bottom: 3px solid var(--navy-edge);
    border-left: 3px solid var(--navy-edge);
    box-shadow: 0 10px 24px rgba(0,0,0,0.18);
  }
  /* Front */
  .card--front { background: var(--paper); }
  .front__mark {
    position: absolute;
    left: 44px;
    top: 96px;
    width: 160px;
    display: flex;
    align-items: center;
    gap: 8px;
    color: var(--navy);
    font-weight: 700;
    font-size: 19px;
    line-height: 1.1;
  }
  .front__mark-dot {
    width: 16px; height: 16px; border-radius: 50%;
    background: var(--navy); flex: none;
  }
  .front__divider {
    position: absolute;
    left: 222px;
    top: 70px;
    width: 1px;
    height: 118px;
    background: var(--navy);
  }
  .front__details {
    position: absolute;
    left: 246px;
    top: 66px;
    color: var(--ink-blue);
  }
  .front__name {
    margin: 0;
    font-size: 22px;
    font-weight: 700;
    color: var(--navy);
  }
  .front__role, .front__taxi {
    margin: 2px 0 0;
    font-size: 16px;
    font-weight: 400;
  }
  .front__taxi { margin-top: 8px; }
  .contact {
    list-style: none;
    margin: 12px 0 0;
    padding: 0;
    font-size: 15px;
  }
  .contact li {
    display: flex;
    align-items: center;
    gap: 8px;
    margin-bottom: 4px;
  }
  .contact svg { width: 13px; height: 13px; flex: none; }
  .front__tagline {
    position: absolute;
    left: 246px;
    bottom: 26px;
    margin: 0;
    font-size: 19px;
    font-weight: 700;
    color: var(--navy);
    letter-spacing: 0.2px;
  }
  /* Back */
  .card--back { background: var(--charcoal); }
  .back__photo {
    position: absolute;
    left: 0; top: 0;
    width: 330px;
    height: 100%;
    background:
      linear-gradient(90deg, rgba(58,58,58,0) 55%, var(--charcoal) 100%),
      linear-gradient(180deg, #b9b4b2 0%, #c99aa8 30%, #e07fb3 55%, #9a9a9a 75%, #bdbdbd 100%);
  }
  .back__mark {
    position: absolute;
    right: 70px;
    top: 78px;
    display: flex;
    align-items: center;
    gap: 10px;
    color: var(--faint);
    font-size: 30px;
    font-weight: 700;
  }
  .back__mark-dot {
    width: 22px; height: 22px; border-radius: 50%;
    background: var(--faint);
  }
  .back__tagline {
    position: absolute;
    right: 40px;
    bottom: 60px;
    margin: 0;
    color: #ffffff;
    font-size: 20px;
    font-weight: 500;
    letter-spacing: 0.3px;
  }
</style>
</head>
<body>
<main class="sheet">
  <section class="card card--front">
    <div class="front__mark"><span class="front__mark-dot"></span><span>Island Watch</span></div>
    <div class="front__divider"></div>
    <div class="front__details">
      <h1 class="front__name">Desmond Arlow</h1>
      <p class="front__role">Retired Police Officer</p>
      <p class="front__taxi">Taxi #T2718</p>
      <ul class="contact">
        <li>
          <svg viewBox="0 0 16 16" aria-hidden="true"><path d="M3 1h3l1.5 4-2 1.2a9 9 0 0 0 4.3 4.3L11 8.5l4 1.5v3a2 2 0 0 1-2 2A12 12 0 0 1 1 3a2 2 0 0 1 2-2z" fill="#123f86"/></svg>
          <span>1-441-555-0142</span>
        </li>
        <li>
          <svg viewBox="0 0 16 16" aria-hidden="true"><rect x="1" y="3" width="14" height="10" fill="none" stroke="#123f86" stroke-width="1.6"/><path d="M1 3l7 6 7-6" fill="none" stroke="#123f86" stroke-width="1.6"/></svg>
          <span>darlow214@mailbox.com</span>
        </li>
      </ul>
    </div>
    <p class="front__tagline">BERMUDA TAXI OPERATOR</p>
  </section>

  <section class="card card--back">
    <div class="back__photo" role="img" aria-label="Photo of a pink taxi van parked at a kerb on a Bermuda street with pastel buildings behind"></div>
    <div class="back__mark"><span class="back__mark-dot"></span><span>Island Watch</span></div>
    <p class="back__tagline">BERMUDA TAXI OPERATOR</p>
  </section>
</main>
</body>
</html>
```